Vorta Session Pass

**DESIGNERS PLEASE READ BRIEF, the ONES that were SUBMITTED does NOT HAVE THE REQUIREMENTS WE ASKED FOR

WE need a card that has the following:

- our LOGO
-Business info (email,phone,website etc)
- SMALL icons (either 3,5,10,15,20) where we can punch a hole to show how many classes our customers have attended
- a place to write the clients name and date of when they paid for the session pass
-an area to write - "This card is valid for the person who's name is on the front only and for a period of 8-40 weeks from date of purchase."

Front of card:
- Logo
- Session number and price" Can be redeemed with any class, check our schedule online.
- website:www.quellomotion.net.au
- Session hole punches (kettlebells or dumbbells)
- Name and date
- "Outdoor Group Fitness Classes"
Back of card:
- Vorta Logo and KESN logo
- email:info@quellomotion.net.au
- phone:0473 926 504
- Address: Pellbrook Oval, Marrowdale. Tarrant Creek Way/Holloway Dr
- Session number and price per session

I've attached our logo and the pricing for our classes.
I request the 20 class pass be made first just to ensure it all fits in well then we can look to delete boxes or kettlebells to adjust to the smaller class passes accordingly down the track. General colours we are thinking is black and green to match our logo and a stencil font or something similar.

Thanks in advance guys.
Updates

Please read project overview. We require a loyalty card/session pass card. So each time a client comes to one of our sessions we need to punch a hole in the card to indicate that they have come. We would like a design for a 20 session pass card made first. Can you utilize a kettle bell or dumbbell for indicating 20 sessions and we will punch a hole in them. We want the Vorta logo central on front and back, KESN logo on the back. All info in initial overview and request. Hope this makes sense, regards Glen.

Industry/Entity Type

Business

Requirements
Must have
• - SMALL icons (either 3,5,10,15,20) where we can punch a hole to show how many classes our customers have attended

```html
<!DOCTYPE html>
<html lang="en">
<head>
<meta charset="utf-8">
<title>Vorta Session Pass</title>
<link rel="stylesheet" href="https://fonts.googleapis.com/css2?family=Oswald:wght@400;600;700&family=Open+Sans:wght@400;600&display=swap">
<style>
  :root {
    --green: #3bb54a;
    --ink: #1b1b1b;
    --grey: #d9d9d9;
    --grey-light: #eeeeee;
    --grey-dark: #9a9a9a;
    --paper: #ffffff;
    --backdrop: #ecebe7;
  }
  * { box-sizing: border-box; margin: 0; padding: 0; }
  html, body { width: 1200px; height: 1024px; overflow: hidden; background: var(--backdrop); }
  body { position: relative; font-family: "Open Sans", sans-serif; color: var(--ink); }

  .card {
    position: absolute; left: 180px; width: 840px; height: 470px;
    background: var(--paper); box-shadow: 0 6px 18px rgba(0,0,0,.18);
    overflow: hidden;
  }
  .card--front { top: 30px; }
  .card--back { top: 524px; }

  .brand {
    position: absolute; display: flex; align-items: center; gap: 12px;
    font-family: "Oswald", sans-serif; font-weight: 700; color: var(--green);
    font-size: 40px; letter-spacing: 2px; text-transform: uppercase; line-height: 1;
  }
  .brand__dot { width: 38px; height: 38px; border-radius: 50%; background: var(--green); flex: none; }

  /* Front */
  .card--front .brand { left: 40px; top: 44px; }
  .tagline { position: absolute; right: 40px; top: 30px; text-align: right; font-family: "Oswald", sans-serif; line-height: 1.25; }
  .tagline__title { font-size: 24px; font-weight: 600; }
  .tagline__web { font-size: 28px; font-weight: 700; letter-spacing: 1px; }
  .tagline__web span { color: var(--green); }

  .punch-table { position: absolute; left: 40px; top: 130px; width: 760px; border-collapse: collapse; font-family: "Oswald", sans-serif; }
  .punch-table th, .punch-table td { border: 1.5px solid var(--ink); height: 40px; font-size: 18px; }
  .punch-table th { background: var(--green); font-weight: 400; text-align: center; }
  .punch-table .col-name { width: 330px; }
  .punch-table .col-date { width: 230px; }
  .punch-table .col-count { width: 70px; text-align: center; background: var(--grey-light); }
  .punch-table .col-hole, .punch-table th.col-hole { background: var(--grey-dark); text-align: center; }
  .hole { display: inline-block; width: 24px; height: 24px; border-radius: 50%; background: #fff; border: 1.5px solid var(--ink); vertical-align: middle; }

  .validity { position: absolute; left: 40px; right: 40px; bottom: 30px; text-align: center; font-size: 20px; line-height: 1.4; }

  /* Back */
  .card--back .brand { right: 40px; top: 46px; }
  .contact { position: absolute; left: 40px; top: 34px; list-style: none; font-size: 18px; }
  .contact li { display: flex; align-items: center; gap: 12px; margin-bottom: 8px; }
  .contact svg { width: 22px; height: 22px; flex: none; fill: var(--green); }

  .pricing { position: absolute; left: 40px; top: 200px; width: 520px; border-collapse: collapse; font-family: "Oswald", sans-serif; font-size: 17px; }
  .pricing caption { background: var(--grey); border: 1.5px solid var(--ink); border-bottom: 0; font-size: 22px; font-weight: 600; padding: 4px 0; }
  .pricing td { border: 1.5px solid var(--ink); padding: 1px 10px; height: 30px; }
  .pricing tr:nth-child(odd) td { background: var(--green); }
  .pricing tr:nth-child(even) td { background: var(--grey); }
  .pricing td.price, .pricing tr.casual td { text-align: center; }

  .partner-badge { position: absolute; right: 60px; bottom: 50px; width: 96px; height: 96px; border-radius: 50%; border: 3px solid var(--ink); }
</style>
</head>
<body>

<section class="card card--front" aria-label="Session pass front">
  <div class="brand"><span class="brand__dot"></span>Vorta Fitness</div>
  <div class="tagline">
    <p class="tagline__title">“Outdoor Group Fitness Classes”</p>
    <p class="tagline__web">WWW.<span>QUELLOMOTION</span>.NET.AU</p>
  </div>

  <table class="punch-table">
    <tr><th class="col-name">Name</th><th class="col-date">Date</th><th class="col-count">Sessions</th><th class="col-hole"><span class="hole"></span></th></tr>
    <tr><td></td><td></td><td class="col-count">3</td><td class="col-hole"><span class="hole"></span></td></tr>
    <tr><td></td><td></td><td class="col-count">5</td><td class="col-hole"><span class="hole"></span></td></tr>
    <tr><td></td><td></td><td class="col-count">10</td><td class="col-hole"><span class="hole"></span></td></tr>
    <tr><td></td><td></td><td class="col-count">15</td><td class="col-hole"><span class="hole"></span></td></tr>
    <tr><td></td><td></td><td class="col-count">20</td><td class="col-hole"><span class="hole"></span></td></tr>
  </table>

  <p class="validity">This card is valid for the person who’s name is on the front only and for<br>a period of 8-40 weeks from date of purchase.</p>
</section>

<section class="card card--back" aria-label="Session pass back">
  <ul class="contact">
    <li><svg viewBox="0 0 24 24"><path d="M6.6 10.8a15.1 15.1 0 0 0 6.6 6.6l2.2-2.2a1 1 0 0 1 1-.25 11.4 11.4 0 0 0 3.6.57 1 1 0 0 1 1 1V20a1 1 0 0 1-1 1A17 17 0 0 1 3 4a1 1 0 0 1 1-1h3.5a1 1 0 0 1 1 1c0 1.25.2 2.45.57 3.57a1 1 0 0 1-.25 1z"/></svg>0473 926 504</li>
    <li><svg viewBox="0 0 24 24"><path d="M2 5h20v14H2z M2 5l10 8 10-8" stroke="#fff" stroke-width="1.5"/></svg>info@quellomotion.net.au</li>
    <li><svg viewBox="0 0 24 24"><circle cx="12" cy="12" r="10"/><path d="M2 12h20M12 2c3 3 3 17 0 20M12 2c-3 3-3 17 0 20" stroke="#fff" stroke-width="1.3" fill="none"/></svg>www.quellomotion.net.au</li>
    <li><svg viewBox="0 0 24 24"><path d="M12 2a7 7 0 0 0-7 7c0 5 7 13 7 13s7-8 7-13a7 7 0 0 0-7-7zm0 9.5A2.5 2.5 0 1 1 12 6.5a2.5 2.5 0 0 1 0 5z"/></svg>Pellbrook Oval, Marrowdale.<br>Tarrant Creek Way/Holloway Dr</li>
  </ul>

  <div class="brand"><span class="brand__dot"></span>Vorta Fitness</div>

  <table class="pricing">
    <caption>Vorta Fitness Pricing</caption>
    <tr class="casual"><td colspan="2">Casual - $12</td></tr>
    <tr><td>3 Session Pass</td><td class="price">$30 ($10 a class)</td></tr>
    <tr><td>5 Session Pass</td><td class="price">$45 ($9 a class)</td></tr>
    <tr><td>10 Session Pass</td><td class="price">$80 ($8 a class)</td></tr>
    <tr><td>15 Session Pass</td><td class="price">$105 ($7 a class)</td></tr>
    <tr><td>20 Session Pass</td><td class="price">$120 ($6 a class)</td></tr>
  </table>

  <div class="partner-badge" role="img" aria-label="KESN partner badge"></div>
</section>

</body>
</html>
```